Poster Design Project

We need a poster designed for of range of products, We would like the 7 suitcases on a police line up style wall, maybe a brick style and they are in the spotlight with a heading of The Unusual Suspects.. then smaller maybe along the bottom Not All Luggage Is The Same.. Stand Out From the Crowd..
I have the images of the cases and need this soon, it must be modern and very cool looking. let me know if you have any questions.
Target Market(s)
this is for Ladies 15 - 55 or store owners.
Industry/Entity Type
Crowd
Look and feel

```html
<!DOCTYPE html>
<html lang="en">
<head>
<meta charset="utf-8">
<title>The Unusual Suspects</title>
<link href="https://fonts.googleapis.com/css2?family=Anton&family=Alegreya+Sans:wght@400&display=swap" rel="stylesheet">
<style>
  :root {
    --ink-black: #05080c;
    --glow-blue: #3a97d8;
    --deep-blue: #12507f;
    --swoosh-blue: #4aa3e0;
    --title-white: #ffffff;
    --title-lime: #b4d334;
    --case-white: #f3f5f7;
    --case-sky: #bcd9ee;
    --case-dark: #2a2d31;
    --hardware: #1c1f23;
    --caster: #cfc6b0;
  }
  html, body {
    margin: 0;
    padding: 0;
    width: 1200px;
    height: 849px;
    overflow: hidden;
    background: var(--ink-black);
  }
  .poster {
    position: relative;
    width: 1200px;
    height: 849px;
    overflow: hidden;
    background:
      radial-gradient(ellipse 620px 470px at 590px 440px, var(--glow-blue) 0%, #2f86c8 45%, var(--deep-blue) 72%, #0a2236 90%, var(--ink-black) 100%);
  }
  .poster__swooshes {
    position: absolute;
    inset: 0;
  }
  .poster__title {
    position: absolute;
    top: 44px;
    left: 0;
    width: 1200px;
    margin: 0;
    text-align: center;
    font-family: "Anton", sans-serif;
    font-weight: 400;
    font-size: 76px;
    line-height: 1;
    letter-spacing: 0;
    color: var(--title-white);
    text-shadow: 0 3px 6px rgba(0, 0, 0, 0.35);
    transform: scaleY(1.22);
    transform-origin: top center;
  }
  .poster__title-accent {
    color: var(--title-lime);
  }
  .poster__lineup {
    position: absolute;
    left: 0;
    top: 0;
  }
  .poster__tagline {
    position: absolute;
    top: 726px;
    left: 0;
    width: 1200px;
    margin: 0;
    text-align: center;
    font-family: "Alegreya Sans", sans-serif;
    font-size: 27px;
    color: var(--title-white);
  }
  .case__handle { fill: var(--hardware); }
  .case__wheel { fill: var(--hardware); }
  .case__caster { fill: var(--caster); }
</style>
</head>
<body>
<main class="poster">
  <svg class="poster__swooshes" width="1200" height="849" viewBox="0 0 1200 849" aria-hidden="true">
    <path d="M 0 300 C 250 120 700 60 1200 150 L 1200 190 C 700 110 280 170 0 360 Z" fill="var(--swoosh-blue)" opacity="0.18"/>
    <path d="M 780 849 C 980 760 1130 640 1200 520 L 1200 600 C 1120 720 1000 800 880 849 Z" fill="var(--swoosh-blue)" opacity="0.14"/>
  </svg>

  <h1 class="poster__title">The <span class="poster__title-accent">Unusual</span> Suspects..</h1>

  <svg class="poster__lineup" width="1200" height="849" viewBox="0 0 1200 849">
    <defs>
      <linearGradient id="case-white" x1="0" y1="0" x2="0" y2="1">
        <stop offset="0" stop-color="var(--case-white)"/>
        <stop offset="0.5" stop-color="#dfe4e9"/>
        <stop offset="1" stop-color="var(--case-dark)"/>
      </linearGradient>
      <linearGradient id="case-sky" x1="0" y1="0" x2="1" y2="0">
        <stop offset="0" stop-color="#d4e7f4"/>
        <stop offset="1" stop-color="var(--case-sky)"/>
      </linearGradient>
      <linearGradient id="case-wash" x1="0" y1="0" x2="1" y2="0">
        <stop offset="0" stop-color="#ffffff"/>
        <stop offset="1" stop-color="#dfe5ea"/>
      </linearGradient>
      <linearGradient id="reflection-fade" x1="0" y1="0" x2="0" y2="1">
        <stop offset="0" stop-color="#ffffff" stop-opacity="0.3"/>
        <stop offset="1" stop-color="#ffffff" stop-opacity="0"/>
      </linearGradient>
    </defs>

    <g class="lineup__reflections" fill="url(#reflection-fade)">
      <rect x="183" y="584" width="90" height="46" rx="6"/>
      <rect x="269" y="584" width="96" height="46" rx="6"/>
      <rect x="360" y="584" width="125" height="52" rx="6"/>
      <rect x="480" y="584" width="242" height="62" rx="8"/>
      <rect x="716" y="584" width="129" height="52" rx="6"/>
      <rect x="843" y="584" width="88" height="46" rx="6"/>
      <rect x="926" y="584" width="84" height="46" rx="6"/>
    </g>

    <g class="lineup__cases">
      <!-- far left, small tower print -->
      <g class="case case--small">
        <rect class="case__handle" x="210" y="369" width="36" height="7" rx="3"/>
        <rect role="img" aria-label="Small hard-shell suitcase printed with a black and white tower photograph" x="183" y="375" width="90" height="173" rx="8" fill="url(#case-white)"/>
        <rect class="case__caster" x="186" y="546" width="10" height="8"/>
        <circle class="case__wheel" cx="191" cy="561" r="7"/>
        <rect class="case__caster" x="260" y="546" width="10" height="8"/>
        <circle class="case__wheel" cx="265" cy="561" r="7"/>
      </g>
      <!-- far right, small washer print -->
      <g class="case case--small">
        <rect class="case__handle" x="951" y="374" width="34" height="7" rx="3"/>
        <rect role="img" aria-label="Small white hard-shell suitcase printed as a washing machine" x="926" y="380" width="84" height="168" rx="8" fill="url(#case-wash)"/>
        <rect class="case__caster" x="929" y="546" width="10" height="8"/>
        <circle class="case__wheel" cx="934" cy="561" r="7"/>
        <rect class="case__caster" x="997" y="546" width="10" height="8"/>
        <circle class="case__wheel" cx="1002" cy="561" r="7"/>
      </g>
      <!-- medium sky -->
      <g class="case case--medium">
        <rect class="case__handle" x="297" y="327" width="40" height="8" rx="3"/>
        <rect role="img" aria-label="Medium pale blue hard-shell suitcase" x="269" y="334" width="96" height="214" rx="8" fill="url(#case-sky)"/>
        <rect class="case__caster" x="272" y="546" width="11" height="8"/>
        <circle class="case__wheel" cx="278" cy="562" r="8"/>
        <rect class="case__caster" x="351" y="546" width="11" height="8"/>
        <circle class="case__wheel" cx="357" cy="562" r="8"/>
      </g>
      <!-- medium tower print -->
      <g class="case case--medium">
        <rect class="case__handle" x="869" y="333" width="36" height="8" rx="3"/>
        <rect role="img" aria-label="Medium hard-shell suitcase printed with a black and white tower photograph" x="843" y="340" width="88" height="208" rx="8" fill="url(#case-white)"/>
        <rect class="case__caster" x="846" y="546" width="11" height="8"/>
        <circle class="case__wheel" cx="852" cy="562" r="8"/>
        <rect class="case__caster" x="917" y="546" width="11" height="8"/>
        <circle class="case__wheel" cx="923" cy="562" r="8"/>
      </g>
      <!-- large washer print -->
      <g class="case case--large">
        <rect class="case__handle" x="400" y="243" width="46" height="9" rx="4"/>
        <rect role="img" aria-label="Large white hard-shell suitcase printed as a washing machine" x="360" y="250" width="125" height="298" rx="10" fill="url(#case-wash)"/>
        <rect class="case__caster" x="365" y="546" width="12" height="9"/>
        <circle class="case__wheel" cx="371" cy="564" r="9"/>
        <rect class="case__caster" x="396" y="546" width="12" height="9"/>
        <circle class="case__wheel" cx="402" cy="564" r="9"/>
      </g>
      <!-- large sky -->
      <g class="case case--large">
        <rect class="case__handle" x="758" y="240" width="46" height="9" rx="4"/>
        <rect role="img" aria-label="Large pale blue hard-shell suitcase" x="716" y="247" width="129" height="301" rx="10" fill="url(#case-sky)"/>
        <rect class="case__caster" x="792" y="546" width="12" height="9"/>
        <circle class="case__wheel" cx="798" cy="564" r="9"/>
        <rect class="case__caster" x="827" y="546" width="12" height="9"/>
        <circle class="case__wheel" cx="833" cy="564" r="9"/>
      </g>
      <!-- centre, largest tower print -->
      <g class="case case--hero">
        <rect class="case__handle" x="550" y="167" width="104" height="10" rx="4"/>
        <rect role="img" aria-label="Largest hard-shell suitcase printed with a black and white tower photograph" x="480" y="176" width="242" height="366" rx="12" fill="url(#case-white)" stroke="#1b1e22" stroke-width="3"/>
        <rect class="case__caster" x="494" y="541" width="14" height="10"/>
        <circle class="case__wheel" cx="501" cy="560" r="10"/>
        <circle class="case__wheel" cx="529" cy="560" r="10"/>
        <rect class="case__caster" x="660" y="541" width="14" height="10"/>
        <circle class="case__wheel" cx="667" cy="560" r="10"/>
        <circle class="case__wheel" cx="697" cy="560" r="10"/>
      </g>
    </g>
  </svg>

  <p class="poster__tagline">Not All Suitcases are the same..Stand out from the crowd.</p>
</main>
</body>
</html>
```